New boutique IT consultancy needs business card

I need a business card and logo for my IT consultancy business, called 'Quenmarlo' . I want it to make me look bigger than I am. I want it to look classy, and modern. Simple design, that will be easy for me to translate into my webpage etc. The business card should be bold, and different.

The logo should emphasise the 'y' as used in quenmarlo

Target Market(s)

IT divisions in other companies

Industry/Entity Type

Business

Contact Information for Business Card

Doreen Pakfield
Director
+61 437 918 205
dpakfield@quenmarlo-mail.test

```html
<!DOCTYPE html>
<html lang="en">
<head>
<meta charset="UTF-8">
<title>Quenmarlo Business Card</title>
<link href="https://fonts.googleapis.com/css2?family=Source+Sans+3:wght@400;600&display=swap" rel="stylesheet">
<style>
  :root {
    --page-bg: #ece9e4;
    --kraft-light: #c9ac82;
    --kraft-mid: #bf9f73;
    --kraft-dark: #b29065;
    --ink: #141210;
  }
  * { margin: 0; padding: 0; box-sizing: border-box; }
  html, body {
    width: 1200px;
    height: 900px;
    overflow: hidden;
    background: var(--page-bg);
    font-family: "Source Sans 3", "Helvetica Neue", Arial, sans-serif;
    color: var(--ink);
  }
  .canvas {
    position: relative;
    width: 1200px;
    height: 900px;
  }
  .card {
    position: absolute;
    width: 556px;
    height: 342px;
    background: radial-gradient(ellipse at 40% 35%, var(--kraft-light) 0%, var(--kraft-mid) 55%, var(--kraft-dark) 100%);
    box-shadow: 0 6px 18px rgba(0, 0, 0, 0.18);
  }
  .card-contact {
    left: 238px;
    top: 62px;
  }
  .card-brand {
    left: 458px;
    top: 518px;
    display: flex;
    align-items: center;
    justify-content: center;
  }
  .contact-block {
    position: absolute;
    left: 0;
    right: 0;
    top: 104px;
    text-align: center;
    line-height: 1.3;
  }
  .person-name {
    font-size: 19px;
    font-weight: 600;
  }
  .person-role {
    font-size: 14px;
    font-weight: 400;
  }
  .contact-lines {
    margin-top: 26px;
    font-size: 15px;
    font-weight: 400;
    line-height: 20px;
  }
  .brand-name {
    font-size: 62px;
    font-weight: 400;
    letter-spacing: 1px;
    color: var(--ink);
    margin-top: 60px;
  }
</style>
</head>
<body>
  <main class="canvas">
    <section class="card card-contact">
      <div class="contact-block">
        <p class="person-name">Doreen Pakfield</p>
        <p class="person-role">Director</p>
        <div class="contact-lines">
          <p class="contact-phone">+61 437 918 205</p>
          <p class="contact-email">dpakfield@quenmarlo-mail.test</p>
          <p class="contact-web">www.quenmarlo-web.test</p>
        </div>
      </div>
    </section>
    <section class="card card-brand">
      <p class="brand-name">Quenmarlo</p>
    </section>
  </main>
</body>
</html>
```